" O projeto zimbo viva é um App para celular no qual o usuário paga uma pequena mensalidade e tem direito a consumir uma bebida por dia nos bares associados. "

```html
<!DOCTYPE html>
<html lang="pt">
<head>
<meta charset="utf-8">
<title>zimbo viva — cartões de visita</title>
<link href="https://fonts.googleapis.com/css2?family=Montserrat:wght@400;500;600;700&display=swap" rel="stylesheet">
<style>
  :root {
    --canvas: #e9e6e1;
    --ink: #161616;
    --paper: #ffffff;
    --corner-blue: #5b8fd0;
    --neon-pink: #e6318f;
    --neon-cyan: #2fb6e6;
    --neon-yellow: #f2e23a;
    --neon-green: #7ed957;
    --neon-violet: #8a5cf0;
    --muted: #6b6b6b;
  }
  html, body {
    margin: 0;
    width: 1200px;
    height: 1200px;
    overflow: hidden;
    background: var(--canvas);
    font-family: "Montserrat", sans-serif;
  }
  .sheet {
    width: 1200px;
    height: 1200px;
    display: flex;
    flex-direction: column;
    align-items: center;
    justify-content: center;
    gap: 70px;
  }
  .card {
    position: relative;
    width: 900px;
    height: 514px;
    overflow: hidden;
    box-shadow: 0 10px 30px rgba(0,0,0,.15);
  }
  .card__corner {
    position: absolute;
    width: 90px;
    height: 90px;
    background: var(--corner-blue);
  }
  /* front */
  .card--front { background: var(--ink); }
  .card--front .card__corner {
    left: 0; bottom: 0;
    clip-path: polygon(0 0, 0 100%, 100% 100%);
  }
  .front__drinks {
    position: absolute;
    left: 250px; top: 120px;
    width: 400px; height: 170px;
    background: linear-gradient(90deg, var(--neon-pink), var(--neon-violet), var(--neon-cyan), var(--neon-green), var(--neon-yellow));
    opacity: .55;
  }
  .front__line {
    position: absolute;
    right: 0; top: 60px;
    width: 230px; height: 3px;
    background: var(--neon-yellow);
  }
  .front__name {
    position: absolute;
    left: 0; right: 0; top: 320px;
    text-align: center;
    color: var(--paper);
    font-weight: 600;
    font-size: 64px;
    letter-spacing: 1px;
  }
  /* back */
  .card--back { background: var(--paper); }
  .card--back .card__corner {
    right: 0; top: 0;
    clip-path: polygon(0 0, 100% 0, 100% 100%);
  }
  .back__info {
    position: absolute;
    left: 70px; top: 60px;
  }
  .back__brand {
    margin: 0;
    font-weight: 600;
    font-size: 34px;
    color: var(--ink);
  }
  .back__person {
    margin: 10px 0 0;
    font-weight: 500;
    font-size: 20px;
    color: var(--neon-violet);
  }
  .back__role {
    margin: 4px 0 22px;
    font-size: 14px;
    color: var(--muted);
  }
  .contact-list { list-style: none; margin: 0; padding: 0; }
  .contact-list li {
    display: flex;
    align-items: center;
    gap: 10px;
    font-size: 14px;
    color: #444;
    margin-bottom: 8px;
  }
  .contact-list svg { width: 18px; height: 18px; }
  .back__rule {
    position: absolute;
    left: 0; bottom: 70px;
    width: 560px; height: 3px;
    background: var(--neon-pink);
  }
  .back__glasses {
    position: absolute;
    right: 90px; bottom: 70px;
    width: 240px; height: 190px;
    background: linear-gradient(160deg, var(--neon-cyan), var(--neon-violet), var(--neon-pink));
    opacity: .45;
  }
</style>
</head>
<body>
<main class="sheet">
  <section class="card card--front" aria-label="Frente do cartão">
    <div class="card__corner"></div>
    <div class="front__line"></div>
    <div class="front__drinks" role="img" aria-label="Ilustração em linhas néon de garrafas e copos"></div>
    <p class="front__name">zimbo viva</p>
  </section>

  <section class="card card--back" aria-label="Verso do cartão">
    <div class="card__corner"></div>
    <div class="back__info">
      <h1 class="back__brand">zimbo viva</h1>
      <p class="back__person">Marina Duarte</p>
      <p class="back__role">Founder / CEO</p>
      <ul class="contact-list">
        <li>
          <svg viewBox="0 0 18 18"><circle cx="9" cy="9" r="8" fill="none" stroke="#999"/><path d="M6 5l2 0 1 2-1 1a5 5 0 0 0 2 2l1-1 2 1v2a1 1 0 0 1-1 1A7 7 0 0 1 5 6a1 1 0 0 1 1-1z" fill="#999"/></svg>
          +55 11 90000 1234
        </li>
        <li>
          <svg viewBox="0 0 18 18"><circle cx="9" cy="9" r="8" fill="none" stroke="#999"/><rect x="5" y="6" width="8" height="6" fill="none" stroke="#999"/><path d="M5 6l4 3 4-3" fill="none" stroke="#999"/></svg>
          marina@zimboviva.com
        </li>
        <li>
          <svg viewBox="0 0 18 18"><circle cx="9" cy="9" r="8" fill="none" stroke="#999"/><circle cx="9" cy="9" r="4.5" fill="none" stroke="#999"/><path d="M4.5 9h9M9 4.5v9" stroke="#999"/></svg>
          www.zimboviva.com
        </li>
      </ul>
    </div>
    <div class="back__rule"></div>
    <div class="back__glasses" role="img" aria-label="Ilustração em linhas néon de copos"></div>
  </section>
</main>
</body>
</html>
```